Rally 84 Training is our company name. and instruction

We provide emergency medical training for CPR (Cardiopulmonary Resuscitation) /AED (Automated External Defibrillation) , BLS (Basic Life Support, First Aid, Bloodborne Pathogens
We travel to the client, give certified (CVL) Continental Vitality League (CVL) instruction for job/industry certification in the areas listed.
CVL Kin and Neighbors noncertified instruction

Target Market(s)

Medical professionals, job required certification

Industry/Entity Type

Medical And Science

Contact Information for Business Card

Logo
Phone, email, address, website address, FB, Instagram

Font styles to use
Serif
Sans Serif

Colors
fff2fe
ff1b2f

Requirements
Must have
• Logo
Course taught: CPR (Cardiopulmonary Resuscitation)
AED (Automated External Defibrillation)
First Aid
BLS (Basic Life Support)
Bloodborne Pathogens
Offsite instruction - we come to you
Nice to have
• Red/Black scheme
Possible ecg/heart rhythm design
Should not have
• Cartoon images

```html
<!DOCTYPE html>
<html lang="en">
<head>
<meta charset="utf-8">
<title>Rally 84 Training – Business Card</title>
<link href="https://fonts.googleapis.com/css2?family=Roboto:wght@400;500;700&display=swap" rel="stylesheet">
<style>
  :root {
    --brand-red: #e8202c;
    --card-black: #1e1c1d;
    --card-white: #ffffff;
    --ink: #1b1b1b;
    --backdrop: #ebebeb;
    --muted-white: #f2f2f2;
  }
  * { box-sizing: border-box; margin: 0; padding: 0; }
  html, body {
    width: 1200px; height: 801px; overflow: hidden;
    background: var(--backdrop);
    font-family: "Roboto", Arial, sans-serif;
  }
  .sheet {
    position: relative; width: 1200px; height: 801px;
  }
  .card {
    position: absolute;
    width: 525px; height: 300px;
    border-bottom: 4px solid var(--brand-red);
    box-shadow: 0 6px 18px rgba(0,0,0,0.18);
    top: 250px;
  }
  /* Front */
  .card--front { left: 50px; background: var(--card-white); color: var(--ink); }
  .brand-mark {
    position: absolute; display: flex; align-items: center; gap: 10px;
  }
  .brand-mark__dot {
    width: 58px; height: 58px; border-radius: 50%;
    background: var(--brand-red);
  }
  .brand-mark__name {
    font-weight: 700; font-size: 20px; color: var(--brand-red);
    white-space: nowrap;
  }
  .card--front .brand-mark { top: 30px; right: 30px; }
  .card--front .rule {
    position: absolute; left: 30px; right: 30px; top: 170px;
    height: 2px; background: var(--ink);
  }
  .person { position: absolute; left: 30px; top: 110px; }
  .person__name { color: var(--brand-red); font-weight: 700; font-size: 24px; line-height: 1.1; }
  .person__role { font-size: 17px; margin-top: 2px; }
  .contact-list { position: absolute; left: 30px; top: 186px; list-style: none; font-size: 17px; line-height: 25px; }
  .contact-list li { display: flex; align-items: center; gap: 12px; }
  .contact-list svg { width: 14px; height: 14px; flex: none; }
  .contact-list .accent { color: var(--brand-red); }
  .address {
    position: absolute; right: 30px; top: 188px; text-align: right;
    font-size: 16px; line-height: 21px;
  }
  /* Back */
  .card--back { left: 625px; background: var(--card-black); color: var(--muted-white); text-align: center; }
  .card--back .brand-mark {
    left: 0; right: 0; top: 28px; flex-direction: column; gap: 8px;
  }
  .card--back .brand-mark__dot { width: 92px; height: 92px; border: 3px solid var(--muted-white); }
  .courses { position: absolute; left: 10px; right: 10px; top: 175px; font-size: 14.5px; line-height: 20px; }
  .courses__title { color: var(--brand-red); font-weight: 700; font-size: 17px; margin-bottom: 2px; }
  .bullet { color: var(--brand-red); }
</style>
</head>
<body>
<main class="sheet">
  <section class="card card--front" aria-label="Business card front">
    <div class="brand-mark">
      <span class="brand-mark__name">Rally 84 Training</span>
      <span class="brand-mark__dot"></span>
    </div>
    <div class="person">
      <p class="person__name">Marcus Hale</p>
      <p class="person__role">Manager</p>
    </div>
    <div class="rule"></div>
    <ul class="contact-list">
      <li>
        <svg viewBox="0 0 16 16" aria-hidden="true"><path d="M4 1 L6.5 4.5 L5 6.5 C6 8.5 7.5 10 9.5 11 L11.5 9.5 L15 12 L13 15 C7 14.5 1.5 9 1 3 Z" fill="var(--brand-red)"/></svg>
        <span>555-014-2100</span>
      </li>
      <li>
        <svg viewBox="0 0 16 16" aria-hidden="true"><rect x="1" y="3" width="14" height="10" fill="none" stroke="var(--brand-red)" stroke-width="1.6"/><path d="M1 3 L8 9 L15 3" fill="none" stroke="var(--brand-red)" stroke-width="1.6"/></svg>
        <span>youremail@mailhub.com</span>
      </li>
      <li>
        <svg viewBox="0 0 16 16" aria-hidden="true"><circle cx="8" cy="8" r="6.5" fill="none" stroke="var(--brand-red)" stroke-width="1.5"/><path d="M1.5 8 H14.5 M8 1.5 V14.5 M8 1.5 C4 5 4 11 8 14.5 M8 1.5 C12 5 12 11 8 14.5" fill="none" stroke="var(--brand-red)" stroke-width="1.2"/></svg>
        <span>www.<span class="accent">yourwebsite</span>.com</span>
      </li>
    </ul>
    <p class="address">Your address, city<br>state, ZIP 0000</p>
  </section>

  <section class="card card--back" aria-label="Business card back">
    <div class="brand-mark">
      <span class="brand-mark__dot"></span>
      <span class="brand-mark__name">Rally 84 Training</span>
    </div>
    <div class="courses">
      <p class="courses__title">Course taught:</p>
      <p>CPR (Cardiopulmonary Resuscitation)</p>
      <p>AED (Automated External Defibrillation) <span class="bullet">●</span> First Aid</p>
      <p>BLS (Basic Life Support) <span class="bullet">●</span> Bloodborne Pathogens</p>
      <p>Offsite instruction - we come to you</p>
    </div>
  </section>
</main>
</body>
</html>
```